Thornfield Marsh, LLC Website

We are a small law firm in need of a website that contains the following:
1. Attractive main page
2. About us/attorney info for three people: Leonard Thornfield (attorney), Brent Marsh (attorney), and Melinda Carrow (legal assistant). We have bio's ready to submit.
3. Blog/video page. We'd like to post blogs and videos to help drive traffic
4. Multidistrict Litigation and Class Actions page, where we post information regarding active MDLs and Class actions that we are doing intake on.
Updates

Can you also please use the color "gold" in the design and logo? Thanks.

Industry/Entity Type

Legal

Coding

Coded - Design and coding required

Number of Pages Required

1 page

Colors
0054AA
0677BA
7BADD7
CADEEF
E8F1F8

Requirements
Must have
• 1. Attractive main page 2. About us/attorney info for three people: Leonard Thornfield (attorney), Brent Marsh (attorney), and Melinda Carrow (legal assistant). We have bio's ready to submit. 3. Blog/video page. We'd like to post blogs and videos to help drive traffic 4. Multidistrict Litigation and Class Actions page, where we post information regarding active MDLs and Class actions that we are doing intake on.

```html
<!DOCTYPE html>
<html lang="en">
<head>
<meta charset="utf-8">
<title>Thornfield Marsh, LLC — Website Pages</title>
<link rel="stylesheet" href="https://fonts.googleapis.com/css2?family=Playfair+Display:wght@400;600;700&family=Lato:wght@400;700&display=swap">
<style>
:root{
  --gold:#c9a23f;
  --ink:#2a2a2a;
  --muted:#7a7a7a;
  --light:#f3f4f6;
  --navy:#2f3f55;
  --navy-deep:#27354a;
  --dark:#2b2b2b;
  --line:#e3e3e3;
  --white:#ffffff;
}
*{margin:0;padding:0;box-sizing:border-box}
html,body{width:1200px;height:467px;overflow:hidden;background:var(--white)}
body{position:relative;font-family:'Lato',sans-serif;color:var(--ink)}
.page{position:absolute;top:22px;height:423px;background:var(--white);border:1px solid #3a3a3a;overflow:hidden}
.page *{position:absolute}
.page .flow,.page .flow *{position:static}
.hero-photo{background:linear-gradient(135deg,#4a4036 0%,#2a2622 55%,#1c1a18 100%)}
.band-photo{background:linear-gradient(90deg,#3c3c3c,#222 60%,#353535)}
.photo{background:linear-gradient(135deg,#b9a58a,#6d5a47 60%,#3d342c)}
.photo.cool{background:linear-gradient(135deg,#cfd6df,#8c96a3 60%,#5b6470)}
.photo.warm{background:linear-gradient(135deg,#e9ddc9,#b8967a 60%,#7a5a45)}
.serif{font-family:'Playfair Display',serif;font-weight:600;color:var(--ink)}
.ctr{left:0;width:100%;text-align:center}
.h-sec{font-size:3.8px}
.h-card{font-size:3px}
.t{font-size:1.6px;line-height:2.3px;color:var(--muted)}
.t.ctr{text-align:center}
.t-light{color:#c9ccd2}
.btn{background:var(--gold);color:var(--white);font-size:1.4px;font-weight:700;letter-spacing:.1px;text-align:center;line-height:4px;height:4px}
.card{background:var(--white);box-shadow:0 .4px 1.6px rgba(0,0,0,.14)}
.grey{background:var(--light)}
.icon{width:4px;height:4px}
.tick{color:var(--gold)}
.nav{white-space:nowrap;font-size:1.5px}
.nav a{font-size:1.5px;color:#555;text-decoration:none;position:static;margin-right:3px}
.field{background:var(--white);border:.3px solid #cfcfcf}
.tag{background:var(--gold);height:1.4px;width:6px}
.play{border-radius:50%;background:rgba(255,255,255,.85)}
</style>
</head>
<body>

<!-- HOME -->
<section class="page" style="left:16px;width:250px">
  <div style="left:0;top:0;width:100%;height:13px;background:var(--white)"></div>
  <div style="left:49px;top:3px;width:5px;height:5px;background:var(--gold)"></div>
  <div class="serif" style="left:55.5px;top:3.8px;font-size:2.6px;color:var(--gold);white-space:nowrap">Thornfield Marsh, LLC</div>
  <div class="nav" style="left:103px;top:5.2px"><a style="color:var(--gold)">HOME</a><a>ABOUT US</a><a>MDL &amp; CLASS ACTIONS</a><a>BLOG &amp; VIDEOS</a><a>CONTACT</a></div>
  <div style="left:184px;top:5px;font-size:1.6px;color:#555;white-space:nowrap">&#9742; (555) 240-8812</div>

  <div class="hero-photo" role="img" aria-label="Law office with scales of justice statue" style="left:0;top:13.5px;width:100%;height:78px"></div>
  <div class="serif ctr" style="top:32px;font-size:7.4px;color:var(--gold)">Professional Legal</div>
  <div class="serif ctr" style="top:44px;font-size:7.4px;color:var(--white)">Representation</div>
  <div class="t ctr" style="top:57px;left:75px;width:100px;color:#e4e4e4">Thornfield &amp; Associates Law Firm is dedicated to protecting your rights and providing expert legal counsel in Multidistrict Litigation and Class Actions.</div>
  <div class="btn" style="left:107px;top:68.5px;width:36px;height:5px;line-height:5px">SCHEDULE A CONSULTATION</div>

  <div class="serif ctr h-sec" style="top:102.5px">Our Legal Expertise</div>
  <div class="t ctr" style="top:110px">We provide comprehensive legal services with a focus on Multidistrict Litigation and Class Actions.</div>
  <div class="card" style="left:49px;top:116px;width:48px;height:36px"></div>
  <div class="card" style="left:102px;top:116px;width:48px;height:36px"></div>
  <div class="card" style="left:153px;top:116px;width:48px;height:36px"></div>
  <svg class="icon" style="left:71px;top:120px" viewBox="0 0 10 10"><rect x="1" y="1" width="6" height="3" fill="#c9a23f" transform="rotate(-35 4 2.5)"/><rect x="4" y="4" width="1.4" height="6" fill="#c9a23f" transform="rotate(-35 4.7 7)"/></svg>
  <svg class="icon" style="left:124px;top:120px" viewBox="0 0 10 10"><circle cx="3" cy="3" r="2" fill="#c9a23f"/><circle cx="7" cy="3" r="2" fill="#c9a23f"/><rect x="0" y="6" width="10" height="4" rx="2" fill="#c9a23f"/></svg>
  <svg class="icon" style="left:175px;top:120px" viewBox="0 0 10 10"><rect x="0" y="3" width="10" height="6.5" rx="1" fill="#c9a23f"/><rect x="3" y="1" width="4" height="2.5" fill="none" stroke="#c9a23f"/></svg>
  <div class="serif ctr h-card" style="left:49px;width:48px;top:126.5px">Multidistrict Litigation</div>
  <div class="serif ctr h-card" style="left:102px;width:48px;top:126.5px">Class Action Lawsuits</div>
  <div class="serif ctr h-card" style="left:153px;width:48px;top:126.5px">Personal Injury</div>
  <div class="t ctr" style="left:52px;width:42px;top:133px">We represent clients in complex MDL cases involving defective products, dangerous drugs, and corporate misconduct.</div>
  <div class="t ctr" style="left:105px;width:42px;top:133px">Our attorneys have extensive experience in class action lawsuits that seek justice for large groups of affected individuals.</div>
  <div class="t ctr" style="left:156px;width:42px;top:133px">We fight for fair compensation for those who have been injured due to negligence or intentional harm.</div>

  <div class="serif h-sec" style="left:49px;top:174px;white-space:nowrap">Why Choose Thornfield &amp; Associates?</div>
  <div class="t" style="left:49px;top:180px;width:74px">At Thornfield &amp; Associates, we combine extensive legal expertise with a client-centered approach to deliver exceptional results.</div>
  <div class="t" style="left:49px;top:188px;width:74px;line-height:4.8px"><span class="tick flow">&#10003;</span> Extensive experience in complex litigation<br><span class="tick flow">&#10003;</span> Personal attention to every case<br><span class="tick flow">&#10003;</span> Commitment to maximizing client recovery<br><span class="tick flow">&#10003;</span> Track record of successful verdicts and settlements<br><span class="tick flow">&#10003;</span> No fee unless we win your case</div>
  <div class="btn" style="left:49px;top:214px;width:30px;height:5px;line-height:5px">LEARN MORE ABOUT US</div>
  <div class="photo" role="img" aria-label="Attorney working at desk with flags behind" style="left:127px;top:173px;width:74px;height:49px"></div>

  <div class="card" style="left:49px;top:226px;width:48px;height:30px"></div>
  <div class="card" style="left:102px;top:226px;width:48px;height:30px"></div>
  <div class="card" style="left:153px;top:226px;width:48px;height:30px"></div>
  <div class="serif ctr h-card" style="left:49px;width:48px;top:231px">Multidistrict Litigation</div>
  <div class="serif ctr h-card" style="left:102px;width:48px;top:231px">Class Action Lawsuits</div>
  <div class="serif ctr h-card" style="left:153px;width:48px;top:231px">Personal Injury</div>
  <div class="t ctr" style="left:52px;width:42px;top:237px">We represent clients in complex MDL cases involving defective products, dangerous drugs, and corporate misconduct.</div>
  <div class="t ctr" style="left:105px;width:42px;top:237px">Our attorneys have extensive experience in class action lawsuits that seek justice for large groups of affected individuals.</div>
  <div class="t ctr" style="left:156px;width:42px;top:237px">We fight for fair compensation for those who have been injured due to negligence or intentional harm.</div>

  <div class="serif h-sec" style="left:49px;top:276px;white-space:nowrap">Why Choose Thornfield &amp; Associates?</div>
  <div class="t" style="left:49px;top:282px;width:74px">At Thornfield &amp; Associates, we combine extensive legal expertise with a client-centered approach to deliver exceptional results.</div>
  <div class="t" style="left:49px;top:290px;width:74px;line-height:4.8px"><span class="tick flow">&#10003;</span> Extensive experience in complex litigation<br><span class="tick flow">&#10003;</span> Personal attention to every case<br><span class="tick flow">&#10003;</span> Commitment to maximizing client recovery<br><span class="tick flow">&#10003;</span> Track record of successful verdicts and settlements<br><span class="tick flow">&#10003;</span> No fee unless we win your case</div>
  <div class="photo" role="img" aria-label="Attorney working at desk with flags behind" style="left:127px;top:275px;width:74px;height:44px"></div>

  <div class="band-photo" role="img" aria-label="Dark desk with legal documents" style="left:0;top:319px;width:100%;height:34px"></div>
  <div class="serif ctr" style="top:324px;font-size:4px;color:var(--white)">Ready to Discuss Your Case?</div>
  <div class="t ctr" style="top:331px;color:#ddd">Contact us today for a free, no-obligation consultation with one of our experienced attorneys.</div>
  <div class="btn" style="left:112px;top:337.5px;width:26px;height:5px;line-height:5px">CONTACT US NOW</div>

  <div style="left:0;top:353px;width:100%;height:70px;background:var(--navy)"></div>
  <div class="serif" style="left:49px;top:360px;font-size:3.3px;color:var(--white);white-space:nowrap">Thornfield Marsh, LLC</div>
  <div class="t t-light" style="left:49px;top:366px;width:44px">Professional legal representation dedicated to protecting your rights and interests.</div>
  <div class="t t-light" style="left:49px;top:372px;width:48px;line-height:4.4px"><span class="tick flow">&#9742;</span> (555) 240-8812<br><span class="tick flow">&#9993;</span> contact@thornfieldmarsh.com<br><span class="tick flow">&#9679;</span> 48 Harbor Row, Suite 210, Millbrook</div>
  <div style="left:49px;top:390px;width:3px;height:3px;border-radius:50%;background:#fff"></div>
  <div style="left:55px;top:390px;width:3px;height:3px;border-radius:50%;background:#fff"></div>
  <div style="left:61px;top:390px;width:3px;height:3px;border-radius:50%;background:#fff"></div>
  <div style="left:67px;top:390px;width:3px;height:3px;border-radius:50%;background:#fff"></div>
  <div class="serif" style="left:102px;top:360px;font-size:3.3px;color:var(--white)">Quick Links</div>
  <div class="t t-light" style="left:102px;top:366px;line-height:4.8px">&#8250; Home<br>&#8250; About Us<br>&#8250; MDL &amp; Class Actions<br>&#8250; Blog &amp; Videos<br>&#8250; Contact</div>
  <div style="left:153px;top:359px;width:48px;height:47px;background:var(--white)"></div>
  <div style="left:157px;top:369px;width:40px;height:4px;background:var(--navy-deep)"></div>
  <div style="left:157px;top:375px;width:40px;height:12px;background:var(--navy-deep)"></div>
  <div class="t" style="left:158px;top:370px;color:#aaa">Your email address</div>
  <div class="t" style="left:158px;top:376px;color:#aaa">Message</div>
  <div class="btn" style="left:157px;top:395px;width:40px">SEND</div>
  <div style="left:49px;top:412px;width:152px;height:11px;background:var(--navy-deep)"></div>
  <div class="t ctr" style="top:416px;color:#ddd">&copy; 2025 Thornfield Marsh, LLC | All Rights Reserved</div>
</section>

<!-- ABOUT -->
<section class="page" style="left:273px;width:274px">
  <div class="band-photo" role="img" aria-label="Law books and gavel on a desk" style="left:0;top:0;width:100%;height:39px"></div>
  <div class="serif ctr" style="top:13.5px;font-size:5.6px;color:var(--white)">About Our Firm</div>
  <div class="t ctr" style="top:23.5px;color:#ddd">Home / <span class="flow" style="color:var(--gold)">About Us</span></div>

  <div class="serif h-sec" style="left:54px;top:52px;font-size:4.3px;white-space:nowrap">Our Commitment to Excellence</div>
  <div class="t" style="left:54px;top:60px;width:80px">Thornfield &amp; Associates Law Firm was founded on the principle that every client deserves exceptional legal representation. For over 15 years, we've fought tirelessly for our clients' rights and have established ourselves as leaders in complex litigation.</div>
  <div class="t" style="left:54px;top:71px;width:80px">Our focus on Multidistrict Litigation and Class Actions allows us to make a significant impact in cases that affect large groups of people who have been harmed by corporate negligence, dangerous products, or unfair business practices.</div>
  <div class="t" style="left:54px;top:82px;width:80px">We believe in a client-centered approach, ensuring that each person we represent receives personalized attention and dedicated service throughout their legal journey.</div>
  <div class="photo cool" role="img" aria-label="Hands reviewing charts on a laptop" style="left:139px;top:50px;width:81px;height:54px"></div>

  <div class="grey" style="left:0;top:118px;width:100%;height:70px"></div>
  <div class="serif ctr h-sec" style="top:129px;font-size:4.3px">Our Core Values</div>
  <div class="card" style="left:54px;top:137px;width:52px;height:41px"></div>
  <div class="card" style="left:111px;top:137px;width:52px;height:41px"></div>
  <div class="card" style="left:168px;top:137px;width:52px;height:41px"></div>
  <svg class="icon" style="left:78px;top:143px" viewBox="0 0 10 10"><rect x="4.5" y="1" width="1" height="8" fill="#c9a23f"/><rect x="1" y="2" width="8" height="1" fill="#c9a23f"/><path d="M0 6 L2 3 L4 6 Z M6 6 L8 3 L10 6 Z" fill="#c9a23f"/><rect x="3" y="9" width="4" height="1" fill="#c9a23f"/></svg>
  <svg class="icon" style="left:135px;top:143px" viewBox="0 0 10 10"><path d="M1 6 L5 2 L9 6 L5 9 Z" fill="#c9a23f"/></svg>
  <svg class="icon" style="left:192px;top:143px" viewBox="0 0 10 10"><rect x="1" y="1" width="6" height="3" fill="#c9a23f" transform="rotate(-35 4 2.5)"/><rect x="4" y="4" width="1.4" height="6" fill="#c9a23f" transform="rotate(-35 4.7 7)"/></svg>
  <div class="serif ctr h-card" style="left:54px;width:52px;top:150px;font-size:3.4px">Integrity</div>
  <div class="serif ctr h-card" style="left:111px;width:52px;top:150px;font-size:3.4px">Compassion</div>
  <div class="serif ctr h-card" style="left:168px;width:52px;top:150px;font-size:3.4px">Excellence</div>
  <div class="t ctr" style="left:57px;width:46px;top:156px">We uphold the highest ethical standards in all our dealings with clients, courts, and opposing counsel.</div>
  <div class="t ctr" style="left:114px;width:46px;top:156px">We understand that our clients are often going through difficult times and approach each case with empathy and support.</div>
  <div class="t ctr" style="left:171px;width:46px;top:156px">We strive for excellence in every aspect of our practice, delivering top-quality legal representation.</div>

  <div class="serif ctr h-sec" style="top:202px;font-size:4.3px">Meet Our Team</div>
  <div class="t ctr" style="top:210px">Our team of experienced legal professionals is dedicated to providing exceptional service and achieving the best possible outcomes for our clients.</div>

  <div class="card" style="left:54px;top:221px;width:52px;height:139px"></div>
  <div class="card" style="left:111px;top:221px;width:52px;height:139px"></div>
  <div class="card" style="left:168px;top:221px;width:52px;height:139px"></div>
  <div class="photo" role="img" aria-label="Portrait of Leonard Thornfield" style="left:66px;top:226px;width:28px;height:28px;border-radius:50%;border:.8px solid var(--gold)"></div>
  <div class="photo" role="img" aria-label="Portrait of Brent Marsh" style="left:123px;top:226px;width:28px;height:28px;border-radius:50%;border:.8px solid var(--gold)"></div>
  <div class="photo" role="img" aria-label="Portrait of Melinda Carrow" style="left:180px;top:226px;width:28px;height:28px;border-radius:50%;border:.8px solid var(--gold)"></div>
  <div class="serif ctr" style="left:54px;width:52px;top:259px;font-size:3.6px">Leonard Thornfield</div>
  <div class="serif ctr" style="left:111px;width:52px;top:259px;font-size:3.6px">Brent Marsh</div>
  <div class="serif ctr" style="left:168px;width:52px;top:259px;font-size:3.6px">Melinda Carrow</div>
  <div class="t ctr" style="left:54px;width:52px;top:265.5px;color:var(--gold)">Founding Attorney</div>
  <div class="t ctr" style="left:111px;width:52px;top:265.5px;color:var(--gold)">Attorney</div>
  <div class="t ctr" style="left:168px;width:52px;top:265.5px;color:var(--gold)">Legal Assistant</div>
  <div class="t ctr" style="left:57px;width:46px;top:271px">Leonard Thornfield brings over 25 years of legal experience to his role as the founding attorney of Thornfield &amp; Associates. After graduating with honors from law school, he began his career at a prestigious national law firm where he specialized in complex litigation.<br><br>In 2008, Leonard founded the firm with a vision to provide client-focused representation in Multidistrict Litigation and class actions. His exceptional track record includes numerous multimillion-dollar verdicts and settlements that have made a significant impact for his clients.<br><br>He is admitted to practice in multiple federal courts and has been recognized as a leading lawyer for consecutive years. He frequently speaks at legal conferences and has published numerous articles on complex litigation strategies.</div>
  <div class="t ctr" style="left:114px;width:46px;top:271px">Brent Marsh joined Thornfield &amp; Associates in 2015 after establishing himself as a skilled litigator at the District Attorney's office. A graduate of a leading law school, he brings unique insight and perspective to complex cases through his background in both criminal and civil litigation.<br><br>Brent specializes in pharmaceutical litigation and medical device cases, where his attention to detail and scientific background have proven invaluable. His meticulous approach to case preparation has resulted in numerous favorable outcomes for the firm's clients.<br><br>As an active member of the state justice association, Brent remains at the forefront of evolving litigation strategies. He has been recognized as a rising star by peers.</div>
  <div class="t ctr" style="left:171px;width:46px;top:271px">Melinda Carrow is the backbone of Thornfield &amp; Associates' daily operations. With over 15 years of experience in the legal field, Melinda's exceptional organizational skills and dedication to client service ensure that all aspects of case management run smoothly.<br><br>Melinda holds a bachelor's degree in Legal Studies and is a certified paralegal. Her expertise in case preparation, document management, and client relations is invaluable to the firm. Clients frequently praise her responsiveness and compassionate approach.<br><br>Beyond her role as a legal assistant, Melinda coordinates the firm's community outreach efforts and pro bono initiatives, reflecting her commitment to making legal services accessible to all.</div>
  <div style="left:75px;top:352px;width:2px;height:2px;background:#555"></div>
  <div style="left:79px;top:352px;width:2px;height:2px;background:#555"></div>
  <div style="left:132px;top:352px;width:2px;height:2px;background:#555"></div>
  <div style="left:136px;top:352px;width:2px;height:2px;background:#555"></div>
  <div style="left:193px;top:352px;width:2px;height:2px;background:#555"></div>

  <div class="band-photo" role="img" aria-label="Dark desk with legal documents" style="left:0;top:371px;width:100%;height:52px"></div>
  <div class="serif ctr" style="top:384px;font-size:4.4px;color:var(--white)">Ready to Work With Our Team?</div>
  <div class="t ctr" style="top:392px;color:#ddd">Contact us today to schedule a free consultation with one of our experienced attorneys.</div>
  <div class="btn" style="left:124px;top:398.5px;width:26px;height:6px;line-height:6px">CONTACT US NOW</div>
</section>

<!-- MDL & CLASS ACTIONS -->
<section class="page" style="left:554px;width:149px">
  <div class="band-photo" role="img" aria-label="Law books and gavel on a desk" style="left:0;top:0;width:100%;height:21px"></div>
  <div class="serif ctr" style="top:7.5px;font-size:2.9px;color:var(--white)">MDL &amp; Class Actions</div>
  <div class="t ctr" style="top:12px;color:#ccc;font-size:1.2px">Home / MDL &amp; Class Actions</div>

  <div class="serif" style="left:29px;top:28px;font-size:2.2px;width:45px">Experienced Representation in Complex Litigation</div>
  <div class="t" style="left:29px;top:34px;width:44px;font-size:1.2px;line-height:1.7px">At Thornfield &amp; Associates, we specialize in representing clients in Multidistrict Litigation and Class Action lawsuits. These complex cases require specialized knowledge, substantial resources, and a deep commitment to fighting for justice on behalf of many clients.</div>
  <div class="btn" style="left:29px;top:56px;width:22px;height:2.6px;line-height:2.6px;font-size:1px">SCHEDULE A FREE CONSULTATION</div>
  <div class="photo cool" role="img" aria-label="Scales of justice beside a business person" style="left:76px;top:27px;width:44px;height:30px"></div>

  <div class="grey" style="left:0;top:66px;width:100%;height:47px"></div>
  <div class="photo warm" role="img" aria-label="Hands signing a legal document" style="left:29px;top:72px;width:45px;height:27px"></div>
  <div class="serif" style="left:76px;top:74px;font-size:2.2px;white-space:nowrap">What is Multidistrict Litigation?</div>
  <div class="t" style="left:76px;top:78px;width:44px;font-size:1.2px;line-height:1.7px">Multidistrict Litigation is a special procedure used to handle many similar cases filed in different federal courts, consolidating them before one judge.</div>
  <div class="t" style="left:76px;top:86px;width:44px;font-size:1.2px;line-height:2.2px"><span class="tick flow">&#10003;</span> Consolidation of similar cases<br><span class="tick flow">&#10003;</span> Efficient handling of evidence<br><span class="tick flow">&#10003;</span> Shared discovery and expert costs<br><span class="tick flow">&#10003;</span> Individual claims stay separate</div>

  <div class="serif" style="left:29px;top:120px;font-size:2.2px;white-space:nowrap">Understanding Class Action Lawsuits</div>
  <div class="t" style="left:29px;top:124px;width:45px;font-size:1.2px;line-height:1.7px">A class action lets one or more people sue on behalf of a larger group who share similar claims against the same defendant.</div>
  <div class="t" style="left:29px;top:132px;width:45px;font-size:1.2px;line-height:2.2px"><span class="tick flow">&#10003;</span> Numerous affected class members<br><span class="tick flow">&#10003;</span> Common questions of law or fact<br><span class="tick flow">&#10003;</span> Typical claims across the group<br><span class="tick flow">&#10003;</span> Fair and adequate representation</div>
  <div class="photo" role="img" aria-label="Group meeting with flags in background" style="left:76px;top:119px;width:44px;height:29px"></div>

  <div class="grey" style="left:0;top:160px;width:100%;height:100px"></div>
  <div class="serif ctr" style="top:166px;font-size:2.2px">Current MDLs We're Handling</div>
  <div class="t ctr" style="top:169.5px;font-size:1.1px">We are actively accepting new clients in the following cases</div>
  <div class="serif" style="left:29px;top:177px;font-size:1.8px">Defective Medical Device Litigation</div>
  <div class="tag" style="left:29px;top:180px"></div>
  <div class="t" style="left:29px;top:182.5px;width:92px;font-size:1.1px;line-height:1.6px">We are representing patients harmed by defective implants that failed early and required revision surgery. Case status: accepting new clients.</div>
  <div class="serif" style="left:29px;top:199px;font-size:1.8px">Dangerous Pharmaceutical MDL</div>
  <div class="tag" style="left:29px;top:202px"></div>
  <div class="t" style="left:29px;top:204.5px;width:92px;font-size:1.1px;line-height:1.6px">Clients who took a recalled medication and later developed serious side effects may qualify. Case status: accepting new clients.</div>
  <div class="serif" style="left:29px;top:222px;font-size:1.8px">Agricultural Chemical Exposure Litigation</div>
  <div class="tag" style="left:29px;top:225px"></div>
  <div class="t" style="left:29px;top:227.5px;width:92px;font-size:1.1px;line-height:1.6px">Farm workers and residents exposed to a common herbicide who later developed illness may be eligible. Case status: open.</div>
  <div class="serif" style="left:29px;top:244px;font-size:1.8px">Defective Automobile Components Litigation</div>
  <div class="tag" style="left:29px;top:247px"></div>
  <div class="t" style="left:29px;top:249.5px;width:92px;font-size:1.1px;line-height:1.6px">Drivers injured by faulty airbags or braking parts may be entitled to compensation. Case status: accepting new clients.</div>

  <div class="serif ctr" style="top:276px;font-size:2.2px">Current Class Actions We're Handling</div>
  <div class="t ctr" style="top:280px;font-size:1.1px">Join others seeking justice in these active class actions</div>
  <div class="serif" style="left:29px;top:287px;font-size:1.8px">Consumer Data Breach Class Action</div>
  <div class="tag" style="left:29px;top:290px"></div>
  <div class="t" style="left:29px;top:292.5px;width:92px;font-size:1.1px;line-height:1.6px">Customers whose personal data was exposed in a major retail breach may join this action. Status: enrolling members.</div>
  <div class="serif" style="left:29px;top:309px;font-size:1.8px">Unfair Banking Practices Class Action</div>
  <div class="tag" style="left:29px;top:312px"></div>
  <div class="t" style="left:29px;top:314.5px;width:92px;font-size:1.1px;line-height:1.6px">Account holders charged improper overdraft fees may be eligible for a refund. Status: enrolling members.</div>
  <div class="serif" style="left:29px;top:331px;font-size:1.8px">Employment Wage and Hour Class Action</div>
  <div class="tag" style="left:29px;top:334px"></div>
  <div class="t" style="left:29px;top:336.5px;width:92px;font-size:1.1px;line-height:1.6px">Hourly workers denied overtime or meal breaks may recover unpaid wages. Status: enrolling members.</div>

  <div class="grey" style="left:0;top:356px;width:100%;height:67px"></div>
  <div class="serif ctr" style="top:364px;font-size:2.2px">Frequently Asked Questions</div>
  <div class="serif" style="left:44px;top:369.5px;font-size:1.6px">How do I know if I qualify for an MDL or class action?</div>
  <div class="t" style="left:44px;top:372.5px;width:62px;font-size:1px;line-height:1.5px">Qualification depends on your injury or loss and how it links to the case. A free review will tell you.</div>
  <div class="serif" style="left:44px;top:381px;font-size:1.6px">Is there a cost to join an MDL or class action?</div>
  <div class="t" style="left:44px;top:384px;width:62px;font-size:1px;line-height:1.5px">No. We work on contingency, so you pay nothing unless we win.</div>
  <div class="serif" style="left:44px;top:392px;font-size:1.6px">How long do MDL and class action cases typically take?</div>
  <div class="t" style="left:44px;top:395px;width:62px;font-size:1px;line-height:1.5px">Most cases take several years, though some settle sooner.</div>
  <div class="serif" style="left:44px;top:402px;font-size:1.6px">What is the difference between an MDL and a class action?</div>
  <div class="t" style="left:44px;top:405px;width:62px;font-size:1px;line-height:1.5px">An MDL keeps each claim separate; a class action joins them into one.</div>
</section>

<!-- BLOG & VIDEOS -->
<section class="page" style="left:710px;width:215px">
  <div class="band-photo" role="img" aria-label="Law books and gavel on a desk" style="left:0;top:0;width:100%;height:30px"></div>
  <div class="serif ctr" style="top:11px;font-size:4.2px;color:var(--white)">Blog &amp; Videos</div>
  <div class="t ctr" style="top:18.5px;color:#ccc;font-size:1.2px">Home / Blog &amp; Videos</div>

  <div class="serif ctr" style="top:40.5px;font-size:3.2px">Featured Video</div>
  <div class="t ctr" style="top:47px;font-size:1.2px">Watch our latest video about important legal topics</div>
  <div role="img" aria-label="Featured firm video player" style="left:42px;top:51px;width:131px;height:74px;background:linear-gradient(90deg,#1f2a3a,#3a4a5e 55%,#7a8593)"></div>
  <div class="play" style="left:104px;top:84px;width:7px;height:7px"></div>
  <svg style="left:106.6px;top:86px;width:2.4px;height:3px" viewBox="0 0 2 2.5"><path d="M0 0 L2 1.25 L0 2.5Z" fill="#2f3f55"/></svg>
  <div class="btn" style="left:92px;top:127px;width:31px;height:4px;font-size:1.1px">SUBSCRIBE TO OUR CHANNEL</div>

  <div class="grey" style="left:0;top:139px;width:100%;height:166px"></div>
  <div class="serif ctr" style="top:152px;font-size:3.2px">Latest Blog Posts</div>
  <div class="t ctr" style="top:158.5px;font-size:1.2px">Stay informed with our latest legal insights and updates</div>

  <div class="card" style="left:42px;top:163px;width:41px;height:55px"></div>
  <div class="card" style="left:87px;top:163px;width:41px;height:55px"></div>
  <div class="card" style="left:132px;top:163px;width:41px;height:55px"></div>
  <div class="photo warm" role="img" aria-label="Person writing legal notes" style="left:42px;top:163px;width:41px;height:23px"></div>
  <div class="photo" role="img" aria-label="Group of people at a meeting" style="left:87px;top:163px;width:41px;height:23px"></div>
  <div class="photo cool" role="img" aria-label="Prescription forms and pills" style="left:132px;top:163px;width:41px;height:23px"></div>
  <div class="t" style="left:44px;top:188px;font-size:1px">April 2, 2025</div>
  <div class="t" style="left:89px;top:188px;font-size:1px">March 18, 2025</div>
  <div class="t" style="left:134px;top:188px;font-size:1px">March 3, 2025</div>
  <div class="serif" style="left:44px;top:190.5px;width:37px;font-size:1.6px;line-height:2.1px">Understanding Multidistrict Litigation: A Guide for Plaintiffs</div>
  <div class="serif" style="left:89px;top:190.5px;width:37px;font-size:1.6px;line-height:2.1px">The Benefits of Class Action Lawsuits for Consumers</div>
  <div class="serif" style="left:134px;top:190.5px;width:37px;font-size:1.6px;line-height:2.1px">Recent Developments in Pharmaceutical Litigation</div>
  <div class="t" style="left:44px;top:196.5px;width:37px;font-size:1px;line-height:1.5px">An MDL lets courts handle many similar cases at once. Here's what it means for your claim.</div>
  <div class="t" style="left:89px;top:196.5px;width:37px;font-size:1px;line-height:1.5px">Class actions give consumers a voice against large companies that cause widespread harm.</div>
  <div class="t" style="left:134px;top:196.5px;width:37px;font-size:1px;line-height:1.5px">The landscape of drug litigation keeps shifting as new rulings and research appear.</div>
  <div class="t" style="left:44px;top:210px;font-size:1px;color:var(--gold)">Read More &#8594;</div>
  <div class="t" style="left:89px;top:210px;font-size:1px;color:var(--gold)">Read More &#8594;</div>
  <div class="t" style="left:134px;top:210px;font-size:1px;color:var(--gold)">Read More &#8594;</div>

  <div class="card" style="left:42px;top:224px;width:41px;height:60px"></div>
  <div class="card" style="left:87px;top:224px;width:41px;height:60px"></div>
  <div class="card" style="left:132px;top:224px;width:41px;height:60px"></div>
  <div class="photo cool" role="img" aria-label="Tax forms with calculator" style="left:42px;top:224px;width:41px;height:23px"></div>
  <div class="photo warm" role="img" aria-label="Signed agreement paperwork" style="left:87px;top:224px;width:41px;height:23px"></div>
  <div class="photo warm" role="img" aria-label="Settlement papers with pen" style="left:132px;top:224px;width:41px;height:23px"></div>
  <div class="t" style="left:44px;top:249px;font-size:1px">March 5, 2025</div>
  <div class="t" style="left:89px;top:249px;font-size:1px">February 28, 2025</div>
  <div class="t" style="left:134px;top:249px;font-size:1px">February 14, 2025</div>
  <div class="serif" style="left:44px;top:251.5px;width:37px;font-size:1.6px;line-height:2.1px">Navigating the Settlement Process in Mass Tort Cases</div>
  <div class="serif" style="left:89px;top:251.5px;width:37px;font-size:1.6px;line-height:2.1px">Essential Elements of a Successful Product Liability Claim</div>
  <div class="serif" style="left:134px;top:251.5px;width:37px;font-size:1.6px;line-height:2.1px">How Consumer Protection Laws Safeguard Your Rights</div>
  <div class="t" style="left:44px;top:258px;width:37px;font-size:1px;line-height:1.5px">Learn how settlements are reached and what to expect at each stage.</div>
  <div class="t" style="left:89px;top:258px;width:37px;font-size:1px;line-height:1.5px">Strong evidence and clear causation are key to winning product claims.</div>
  <div class="t" style="left:134px;top:258px;width:37px;font-size:1px;line-height:1.5px">Federal and state rules protect buyers from deceptive business practices.</div>
  <div class="t" style="left:44px;top:275px;font-size:1px;color:var(--gold)">Read More &#8594;</div>
  <div class="t" style="left:89px;top:275px;font-size:1px;color:var(--gold)">Read More &#8594;</div>
  <div class="t" style="left:134px;top:275px;font-size:1px;color:var(--gold)">Read More &#8594;</div>
  <div class="btn" style="left:99px;top:289.5px;width:3.5px;height:3.5px;line-height:3.5px;font-size:1.1px">1</div>
  <div class="t" style="left:105px;top:290px;font-size:1.1px;white-space:nowrap">2 &nbsp; 3 &nbsp; &#8250;</div>

  <div class="serif ctr" style="top:312px;font-size:3.2px">Video Library</div>
  <div class="t ctr" style="top:318.5px;font-size:1.2px">Browse our collection of informative legal videos</div>
  <div class="card" style="left:42px;top:324px;width:41px;height:51px"></div>
  <div class="card" style="left:87px;top:324px;width:41px;height:51px"></div>
  <div class="card" style="left:132px;top:324px;width:41px;height:51px"></div>
  <div role="img" aria-label="Video thumbnail" style="left:42px;top:324px;width:41px;height:22px;background:linear-gradient(90deg,#1f2a3a,#4a5666)"></div>
  <div role="img" aria-label="Video thumbnail" style="left:87px;top:324px;width:41px;height:22px;background:linear-gradient(90deg,#1f2a3a,#4a5666)"></div>
  <div role="img" aria-label="Video thumbnail" style="left:132px;top:324px;width:41px;height:22px;background:linear-gradient(90deg,#1f2a3a,#4a5666)"></div>
  <div class="play" style="left:60.5px;top:332.5px;width:4px;height:4px"></div>
  <div class="play" style="left:105.5px;top:332.5px;width:4px;height:4px"></div>
  <div class="play" style="left:150.5px;top:332.5px;width:4px;height:4px"></div>
  <div class="serif" style="left:44px;top:349px;width:37px;font-size:1.6px;line-height:2.1px">Understanding Your Rights in a Class Action</div>
  <div class="serif" style="left:89px;top:349px;width:37px;font-size:1.6px;line-height:2.1px">The MDL Process Explained</div>
  <div class="serif" style="left:134px;top:349px;width:37px;font-size:1.6px;line-height:2.1px">What to Expect During Your Legal Consultation</div>
  <div class="t" style="left:44px;top:355px;width:37px;font-size:1px;line-height:1.5px">Attorney Leonard Thornfield explains what you need to know before joining a class action.</div>
  <div class="t" style="left:89px;top:355px;width:37px;font-size:1px;line-height:1.5px">Attorney Brent Marsh walks through the multidistrict litigation process step by step.</div>
  <div class="t" style="left:134px;top:355px;width:37px;font-size:1px;line-height:1.5px">Our team explains how to prepare for your first meeting with our attorneys.</div>

  <div class="grey" style="left:0;top:383px;width:100%;height:38px"></div>
  <div class="serif ctr" style="top:393px;font-size:2.8px">Subscribe to Our Newsletter</div>
  <div class="t ctr" style="top:398.5px;font-size:1.1px">Stay updated with our latest blog posts, videos, and case updates by subscribing to our newsletter.</div>
  <div class="field" style="left:79px;top:402px;width:40px;height:4px"></div>
  <div class="t" style="left:81px;top:402.8px;font-size:1px">Your email address</div>
  <div class="btn" style="left:119px;top:402px;width:16px;font-size:1px">SUBSCRIBE</div>
  <div style="left:0;top:421px;width:100%;height:2px;background:var(--navy)"></div>
</section>

<!-- CONTACT -->
<section class="page" style="left:932px;width:252px">
  <div class="band-photo" role="img" aria-label="Law books and gavel on a desk" style="left:0;top:0;width:100%;height:31px"></div>
  <div class="serif ctr" style="top:9px;font-size:4.6px;color:var(--white)">Contact Us</div>
  <div class="t ctr" style="top:17.5px;color:#ccc;font-size:1.2px">Home / <span class="flow" style="color:var(--gold)">Contact</span></div>

  <div class="serif ctr" style="top:42.5px;font-size:3.8px">Get In Touch</div>
  <div class="t ctr" style="top:49.5px;font-size:1.3px">Our team is ready to provide the expert legal guidance you need.</div>
  <div class="card" style="left:49px;top:56px;width:49px;height:38px"></div>
  <div class="card" style="left:102px;top:56px;width:49px;height:38px"></div>
  <div class="card" style="left:154px;top:56px;width:49px;height:38px"></div>
  <div class="ctr" style="left:49px;width:49px;top:60px;font-size:3.6px;color:var(--gold)">&#9742;</div>
  <div class="ctr" style="left:102px;width:49px;top:60px;font-size:3.6px;color:var(--gold)">&#9993;</div>
  <svg style="left:176.5px;top:60.5px;width:4px;height:4.6px" viewBox="0 0 10 12"><path d="M5 12 C2 8 0 6 0 5 A5 5 0 0 1 10 5 C10 6 8 8 5 12Z" fill="#c9a23f"/><circle cx="5" cy="5" r="2" fill="#fff"/></svg>
  <div class="serif ctr" style="left:49px;width:49px;top:67.5px;font-size:3px">Call Us</div>
  <div class="serif ctr" style="left:102px;width:49px;top:67.5px;font-size:3px">Email Us</div>
  <div class="serif ctr" style="left:154px;width:49px;top:67.5px;font-size:3px">Visit Us</div>
  <div class="t ctr" style="left:49px;width:49px;top:74px;font-size:1.3px;line-height:2.6px">(555) 240-8812<br>Monday - Friday: 8:00 AM - 6:00 PM</div>
  <div class="t ctr" style="left:102px;width:49px;top:74px;font-size:1.3px;line-height:2.6px">contact@thornfieldmarsh.com<br>We respond to all inquiries within 24 hours.</div>
  <div class="t ctr" style="left:154px;width:49px;top:74px;font-size:1.3px;line-height:2.6px">48 Harbor Row, Suite 210, Millbrook<br>Free parking available on premises.</div>
  <div class="t ctr" style="left:49px;width:49px;top:82px;font-size:1.2px;color:var(--gold)">Call Now</div>
  <div class="t ctr" style="left:102px;width:49px;top:82px;font-size:1.2px;color:var(--gold)">Send Email</div>
  <div class="t ctr" style="left:154px;width:49px;top:82px;font-size:1.2px;color:var(--gold)">Get Directions</div>

  <div class="grey" style="left:0;top:111px;width:100%;height:114px"></div>
  <div class="serif ctr" style="top:123px;font-size:3.8px">Send Us a Message</div>
  <div class="t ctr" style="top:130px;font-size:1.3px">Complete the form below for a free, confidential consultation.</div>
  <div class="card" style="left:74px;top:135px;width:105px;height:83px"></div>
  <div class="t" style="left:78px;top:139px;font-size:1.2px;color:#333">Full Name*</div>
  <div class="t" style="left:128px;top:139px;font-size:1.2px;color:#333">Email Address*</div>
  <div class="field" style="left:78px;top:142px;width:47px;height:5px"></div>
  <div class="field" style="left:128px;top:142px;width:47px;height:5px"></div>
  <div class="t" style="left:78px;top:152.5px;font-size:1.2px;color:#333">Phone Number*</div>
  <div class="t" style="left:128px;top:152.5px;font-size:1.2px;color:#333">Case Type*</div>
  <div class="field" style="left:78px;top:156px;width:47px;height:5px"></div>
  <div class="field" style="left:128px;top:156px;width:47px;height:5px"></div>
  <div class="t" style="left:129.5px;top:157.3px;font-size:1.1px">Select Case Type</div>
  <div class="t" style="left:172px;top:157px;font-size:1.1px">&#9662;</div>
  <div class="t" style="left:78px;top:166px;font-size:1.2px;color:#333">Message*</div>
  <div class="field" style="left:78px;top:169.5px;width:97px;height:17px"></div>
  <div style="left:78px;top:191px;width:1.5px;height:1.5px;border:.3px solid #888"></div>
  <div class="t" style="left:81px;top:190.5px;width:92px;font-size:1.1px;line-height:1.7px">I agree that submitting this form does not create an attorney-client relationship and all information submitted will remain confidential.</div>
  <div class="btn" style="left:114px;top:200px;width:25px;font-size:1.1px">SUBMIT REQUEST</div>

  <div class="serif ctr" style="top:238px;font-size:3.8px">Our Location</div>
  <div role="img" aria-label="Office location map" style="left:49px;top:247px;width:154px;height:60px;background:#1e1e1e"></div>
  <div class="t" style="left:51px;top:249px;font-size:1.1px;color:#ddd;font-family:monospace;white-space:nowrap">Map service rejected your request. Invalid request. Invalid 'pb' parameter.</div>

  <div class="grey" style="left:0;top:316px;width:100%;height:107px"></div>
  <div class="serif ctr" style="top:327px;font-size:3.8px">Frequently Asked Questions</div>
  <div class="serif" style="left:74px;top:336px;font-size:2.9px;white-space:nowrap">What should I bring to my initial consultation?</div>
  <div class="t" style="left:74px;top:342.5px;width:104px;font-size:1.2px;line-height:1.9px">For your initial consultation, please bring any relevant documents, such as medical records, correspondence with insurance companies, and any other materials related to your case. This will help our attorneys better understand your situation.</div>
  <div class="serif" style="left:74px;top:358px;font-size:2.9px;white-space:nowrap">Is there a fee for the initial consultation?</div>
  <div class="t" style="left:74px;top:364.5px;width:104px;font-size:1.2px;line-height:1.9px">No, we offer free initial consultations for all potential clients. During this consultation, we will evaluate your case and discuss your legal options without any cost or obligation.</div>
  <div class="serif" style="left:74px;top:376px;font-size:2.9px;white-space:nowrap">How soon should I contact an attorney after an incident?</div>
  <div class="t" style="left:74px;top:382.5px;width:104px;font-size:1.2px;line-height:1.9px">It's best to contact an attorney as soon as possible after an incident. There are legal time limits for filing claims, and important evidence can be lost over time. Early consultation allows us to begin investigating your case promptly.</div>
  <div class="serif" style="left:74px;top:398px;font-size:2.9px;white-space:nowrap">Can I speak directly with an attorney about my case?</div>
  <div class="t" style="left:74px;top:404.5px;width:104px;font-size:1.2px;line-height:1.9px">Yes, our attorneys meet personally with clients during consultations. While our legal assistants may gather initial information, you will have the opportunity to discuss your case directly with an experienced attorney.</div>
</section>

</body>
</html>
```